Redesign Application Page for Job Position

Would like to get a redesign on our Job Application Page.
You can use corvanheights or brendolix as references.

http://www.careersatxlm.example/XLM/NCreateAccount.aspx?aga=qtrwkz4hopLM7

Target Market(s)

Professional Security Individuals

Industry/Entity Type

Security Guard

Coding

Coded - Design and coding required

Number of Pages Required

1 page

Font styles to use
Sans Serif

Colors
0255a3
3276b5
ffcf3e
fee18a

Requirements
Must have
• User Friendly, Easy Navigation. Must be very easy to read and understand what is required or missing.
Should not have
• Ugly or Bulky

```html
<!DOCTYPE html>
<html lang="en">
<head>
<meta charset="utf-8">
<title>Create an Application – Xenmark Lookout Marshals, Inc.</title>
<link rel="stylesheet" href="https://fonts.googleapis.com/css2?family=Poppins:wght@400;500;600;700&display=swap">
<style>
:root{
  --blue:#0255a3;
  --blue-mid:#3276b5;
  --yellow:#ffcf3e;
  --yellow-soft:#fee18a;
  --field:#f1f1f1;
  --field-border:#dcdcdc;
  --text:#1d1d1d;
  --muted:#555;
  --red:#e0262b;
  --white:#fff;
}
*{box-sizing:border-box;margin:0;padding:0}
html,body{width:1200px;height:2384px;overflow:hidden}
body{
  font-family:"Poppins",sans-serif;color:var(--text);
  background:linear-gradient(180deg,var(--blue) 0%,#3a7393 35%,#9fa867 65%,var(--yellow) 100%);
  position:relative;
}
.card{position:absolute;left:180px;top:92px;width:839px;height:2112px;background:var(--white);box-shadow:0 6px 22px rgba(0,0,0,.25)}
.brand{position:absolute;top:19px;left:0;width:100%;display:flex;justify-content:center;align-items:center;gap:14px;height:104px}
.brand-mark{width:90px;height:90px;border-radius:50%;background:var(--blue)}
.brand-name{font-size:21px;font-weight:700;line-height:1.35;color:var(--text)}
.band{position:absolute;top:142px;left:0;width:100%;height:56px;background:var(--yellow);display:flex;align-items:center;justify-content:center;font-size:17px;font-weight:600;color:var(--blue)}
.intro{position:absolute;top:215px;width:100%;text-align:center;font-size:13.5px;color:var(--text)}
.req{color:var(--red)}
.row{position:absolute;left:54px;right:54px;height:38px;display:flex;align-items:center}
.label{width:151px;font-size:14.5px;line-height:1.6;flex-shrink:0}
.value{font-size:16px;font-weight:500}
.field{height:38px;background:var(--field);border:1px solid var(--field-border);width:353px;font-size:13px;color:var(--muted);display:flex;align-items:center;padding:0 12px}
.field.wide{width:578px}
.field.short{width:188px}
.select{justify-content:space-between;font-size:12px;font-style:italic}
.select.plain{font-style:normal;font-size:14px}
.caret{width:0;height:0;border-left:4px solid transparent;border-right:4px solid transparent;border-top:5px solid var(--blue)}
.group{display:flex;gap:14px}
.phone{width:285px;font-size:13.5px;color:var(--text);letter-spacing:.5px}
.phone span{color:#777;margin-left:10px;letter-spacing:3px}
.radio{display:flex;align-items:center;gap:6px;font-size:16px;margin-right:22px}
.dot{width:10px;height:10px;border-radius:50%;border:1px solid #aaa;background:#e6e6e6}
.box{width:11px;height:11px;border:1px solid #aaa;background:#eee;display:inline-block}
.section{position:absolute;left:54px;font-size:14.5px;color:var(--blue)}
table{position:absolute;left:54px;width:728px;border-collapse:collapse;font-size:14px}
th{background:var(--yellow);color:var(--white);font-weight:400;text-align:left;height:38px;padding:0 24px;font-size:14px}
td{background:var(--field);border:1px solid var(--white);padding:0 24px;line-height:1.6}
.license td.num,.license td.exp{padding:0 8px}
.license .in{height:32px;background:var(--white);border:1px solid #ccc}
.license .date{display:flex;align-items:center;gap:8px;font-size:13px;color:var(--muted);padding:0 10px}
.shifts th{text-align:center;padding:0}
.shifts th:first-child{text-align:left;padding-left:24px}
.shifts td{text-align:center;height:48px;padding:0;border-color:#dcdcdc}
.shifts td:first-child{text-align:left;padding-left:24px}
.langs{display:grid;grid-template-columns:110px 110px;row-gap:12px;font-size:13px}
.langs label{display:flex;align-items:center;gap:6px}
.actions{position:absolute;top:2020px;width:100%;display:flex;justify-content:center;gap:6px}
.btn{width:159px;height:51px;border-radius:26px;font-size:20px;font-weight:600;display:flex;align-items:center;justify-content:center}
.btn-primary{background:var(--blue);color:var(--white)}
.btn-secondary{background:var(--yellow);color:var(--white)}
.help{position:absolute;top:2232px;width:100%;text-align:center;font-size:17px;font-weight:600;line-height:30px}
.help .title{color:var(--blue)}
.legal{font-size:11px;font-weight:400;margin-top:4px}
</style>
</head>
<body>
<main class="card">
  <header class="brand">
    <div class="brand-mark"></div>
    <div class="brand-name">XENMARK LOOKOUT<br>MARSHALS, INC.</div>
  </header>
  <div class="band">CREATE AN APPLICATION</div>
  <p class="intro">Complete all required fields (<span class="req">*</span>), then click "Continue" to create your account!</p>

  <div class="row" style="top:269px"><span class="label">Date Created:</span><span class="value">04-Jan-2018</span></div>
  <div class="row" style="top:313px"><span class="label">First Name<span class="req">*</span>:</span><div class="field"></div></div>
  <div class="row" style="top:363px"><span class="label">Middle Name:</span><div class="field"></div></div>
  <div class="row" style="top:414px"><span class="label">Last Name<span class="req">*</span>:</span><div class="field"></div></div>
  <div class="row" style="top:466px"><span class="label">Gender :</span>
    <span class="radio"><span class="dot"></span>Male</span><span class="radio"><span class="dot"></span>Female</span></div>
  <div class="row" style="top:514px"><span class="label">D.O.B :</span>
    <div class="group">
      <div class="field select plain" style="width:110px">Month<span class="caret"></span></div>
      <div class="field select plain" style="width:106px">Day<span class="caret"></span></div>
      <div class="field select plain" style="width:106px">Year<span class="caret"></span></div>
    </div></div>
  <div class="row" style="top:569px"><span class="label">Street Address<span class="req">*</span>:</span><div class="field wide"></div></div>
  <div class="row" style="top:622px"><span class="label">City:</span><div class="field"></div></div>
  <div class="row" style="top:674px"><span class="label">State:</span><div class="field select">Select<span class="caret"></span></div></div>
  <div class="row" style="top:725px"><span class="label">Nearest Office:</span><div class="field select">Select<span class="caret"></span></div></div>
  <div class="row" style="top:778px"><span class="label">Zip:</span><div class="field short"></div></div>
  <div class="row" style="top:833px"><span class="label">Phone Number :</span>
    <div class="group" style="gap:8px">
      <div class="field phone">Cell :<span>---- ---- -----</span></div>
      <div class="field phone">Home :<span>---- ---- -----</span></div>
    </div></div>
  <div class="row" style="top:894px"><span class="label">Job Position :</span><div class="field select">Select<span class="caret"></span></div></div>
  <div class="row" style="top:946px"><span class="label">SSN<span class="req">*</span>:</span><div class="field" style="letter-spacing:3px;font-size:14px">___-__-____</div></div>

  <h2 class="section" style="top:1014px;font-weight:400">License Details</h2>
  <table class="license" style="top:1048px">
    <tr><th style="width:340px">Type</th><th style="width:224px">Number</th><th>Expire Date</th></tr>
    <tr style="height:52px"><td>Guard Card</td><td class="num"><div class="in"></div></td><td class="exp"><div class="in date"><span>&#128197;</span>mm/dd/yyyy</div></td></tr>
    <tr style="height:48px"><td>Baton</td><td class="num"><div class="in"></div></td><td class="exp"><div class="in date"><span>&#128197;</span>mm/dd/yyyy</div></td></tr>
    <tr style="height:52px"><td>Gun Permit</td><td class="num"><div class="in"></div></td><td class="exp"><div class="in date"><span>&#128197;</span>mm/dd/yyyy</div></td></tr>
    <tr style="height:67px"><td>Transportation Workers<br>Identification Card (TWIC)</td><td class="num"><div class="in"></div></td><td class="exp"><div class="in date"><span>&#128197;</span>mm/dd/yyyy</div></td></tr>
    <tr style="height:49px"><td>Merchant Mariner Credential (MMC)</td><td class="num"><div class="in"></div></td><td class="exp"><div class="in date"><span>&#128197;</span>mm/dd/yyyy</div></td></tr>
    <tr style="height:91px"><td>Standards of Training, Certification<br>and Watchkeeping for Seafarers<br>(SCTW)</td><td class="num"><div class="in"></div></td><td class="exp"><div class="in date"><span>&#128197;</span>mm/dd/yyyy</div></td></tr>
  </table>

  <div class="row" style="top:1469px"><span class="label">ID Document Type :</span><div class="field select">Select<span class="caret"></span></div></div>
  <div class="row" style="top:1536px;height:52px;align-items:flex-start"><span class="label">Additional<br>Languages :</span>
    <div class="langs">
      <label><span class="box"></span>Spanish</label><label><span class="box"></span>French</label>
      <label><span class="box"></span>Japanese</label><label><span class="box"></span>Chinese</label>
    </div></div>
  <div class="row" style="top:1606px"><span class="label">Email<span class="req">*</span>:</span><div class="field"></div></div>
  <div class="row" style="top:1671px"><span class="label">How did you hear<br>about us?</span><div class="field select">Select<span class="caret"></span></div></div>

  <h2 class="section" style="top:1750px;font-weight:400">Work Availability :</h2>
  <table class="shifts" style="top:1784px">
    <tr><th style="width:170px">Shift</th><th>Sun</th><th>Mon</th><th>Tue</th><th>Wed</th><th>Thu</th><th>Fri</th><th>Sat</th></tr>
    <tr><td>Day Shift</td><td><span class="box"></span></td><td><span class="box"></span></td><td><span class="box"></span></td><td><span class="box"></span></td><td><span class="box"></span></td><td><span class="box"></span></td><td><span class="box"></span></td></tr>
    <tr><td>Swing Shift</td><td><span class="box"></span></td><td><span class="box"></span></td><td><span class="box"></span></td><td><span class="box"></span></td><td><span class="box"></span></td><td><span class="box"></span></td><td><span class="box"></span></td></tr>
    <tr><td>Night Shift</td><td><span class="box"></span></td><td><span class="box"></span></td><td><span class="box"></span></td><td><span class="box"></span></td><td><span class="box"></span></td><td><span class="box"></span></td><td><span class="box"></span></td></tr>
  </table>

  <div class="actions"><span class="btn btn-primary">Continue</span><span class="btn btn-secondary">Discard</span></div>
</main>

<footer class="help">
  <div class="title">Need Help?</div>
  <div>Call us at: (555)014-2290</div>
  <div>and ask for a Human Resource representative.</div>
  <div class="legal">© 2018 All rights are reserved. Privacy | Terms of use</div>
</footer>
</body>
</html>
```